Morvex Business Card (intended for Business Card sized magnet)

Hi guys,

I would like to get a design for my business card for the restaurant. The design must be single sided as I intend to produce business card sized magnets.

The File attached must me on and I'm open for new ides

Can you please ensure that the design meets Cardowell's magnetic business card size specifications:

http://www.cardowell.example.au/custom-magnets.aspx?txi=15695&xnid=TopNav_Magnetic+Business+Cards+(linked+item)_Magnets_Marketing+Products&xnav=TopNav

Full Bleed Size (starting document size):
90 x 52 mm
1062 x 615 pixels
* Finished artwork should use the full bleed dimensions for best results.

Document Trim Size (final size after being cut):
87 x 49 mm
1028 x 579 pixels
* Please be sure to keep all text within the safe margin.

Resolution:
300 DPI

The winning design/source files need to meet these specifications.

Thanks
Updates

Hi guys, can I see more options please Thanks

```html
<!DOCTYPE html>
<html lang="en">
<head>
<meta charset="utf-8">
<title>Morvex Business Card</title>
<link rel="stylesheet" href="https://fonts.googleapis.com/css2?family=Gentium+Book+Plus:ital@0;1&family=Carlito&display=swap">
<style>
  :root {
    --page: #ffffff;
    --card: #dedede;
    --ink: #111111;
    --rule: #1a1a1a;
    --band: #a9a9a9;
    --icon: #1c1c1c;
  }
  html, body {
    margin: 0;
    padding: 0;
    width: 1200px;
    height: 1000px;
    overflow: hidden;
    background: var(--page);
  }
  .canvas {
    position: relative;
    width: 1200px;
    height: 1000px;
  }
  .card {
    position: absolute;
    left: 19px;
    top: 142px;
    width: 1162px;
    height: 673px;
    background: var(--card);
    border: 1.5px solid var(--rule);
    overflow: hidden;
  }
  .divider {
    position: absolute;
    left: 394px;
    top: 0;
    width: 3px;
    height: 100%;
    background: var(--rule);
  }
  .brand-name {
    position: absolute;
    left: 10px;
    top: 59px;
    margin: 0;
    font-family: "Gentium Book Plus", serif;
    font-weight: 400;
    font-size: 110px;
    line-height: 1;
    color: var(--ink);
  }
  .rule {
    position: absolute;
    height: 3px;
    background: var(--rule);
  }
  .rule--brand-top { left: 0; top: 182px; width: 386px; }
  .rule--brand-bottom { left: 0; top: 308px; width: 386px; }
  .rule--footer-top { left: 405px; top: 526px; width: 757px; }
  .rule--footer-bottom { left: 405px; top: 622px; width: 757px; }
  .ornament-band {
    position: absolute;
    background: linear-gradient(180deg, #b8b8b8, var(--band) 50%, #b8b8b8);
  }
  .ornament-band--brand { left: 0; top: 192px; width: 386px; height: 110px; }
  .ornament-band--footer { left: 405px; top: 535px; width: 757px; height: 82px; }
  .contact-list {
    position: absolute;
    left: 46px;
    top: 352px;
    width: 340px;
    margin: 0;
    padding: 0;
    list-style: none;
    font-family: "Carlito", sans-serif;
    font-size: 28px;
    color: var(--ink);
  }
  .contact-item {
    display: flex;
    align-items: flex-start;
    line-height: 46px;
    white-space: nowrap;
  }
  .contact-icon {
    width: 26px;
    height: 46px;
    margin-right: 26px;
    flex: none;
  }
  .contact-icon svg { display: block; width: 26px; height: 46px; }
  .holder {
    position: absolute;
    right: 78px;
    top: 70px;
    text-align: right;
  }
  .holder-name {
    margin: 0 36px 0 0;
    font-family: "Gentium Book Plus", serif;
    font-weight: 400;
    font-size: 50px;
    line-height: 1.1;
    color: var(--ink);
  }
  .holder-title {
    margin: 0;
    font-family: "Gentium Book Plus", serif;
    font-style: italic;
    font-size: 33px;
    line-height: 1.2;
    color: var(--ink);
  }
</style>
</head>
<body>
<div class="canvas">
  <div class="card">
    <h1 class="brand-name">Morvex</h1>
    <div class="rule rule--brand-top"></div>
    <div class="ornament-band ornament-band--brand" role="img" aria-label="Geometric star-and-knot ornamental border with red, teal and yellow centres"></div>
    <div class="rule rule--brand-bottom"></div>

    <ul class="contact-list">
      <li class="contact-item">
        <span class="contact-icon">
          <svg viewBox="0 0 26 46" aria-hidden="true"><path d="M2 24 L13 14 L24 24 L21 24 L21 33 L15 33 L15 27 L11 27 L11 33 L5 33 L5 24 Z" fill="var(--icon)"/><rect x="18" y="15" width="3" height="6" fill="var(--icon)"/></svg>
        </span>
        <span>412, Harwood Lane,<br>Elmbrook North, 3190</span>
      </li>
      <li class="contact-item">
        <span class="contact-icon">
          <svg viewBox="0 0 26 46" aria-hidden="true"><g fill="none" stroke="var(--icon)" stroke-width="2"><circle cx="13" cy="23" r="10"/><ellipse cx="13" cy="23" rx="4.5" ry="10"/><line x1="3" y1="23" x2="23" y2="23"/><line x1="5" y1="17.5" x2="21" y2="17.5"/><line x1="5" y1="28.5" x2="21" y2="28.5"/></g></svg>
        </span>
        <span>www.morvex.com.au</span>
      </li>
      <li class="contact-item">
        <span class="contact-icon">
          <svg viewBox="0 0 26 46" aria-hidden="true"><rect x="2" y="16" width="22" height="15" fill="var(--icon)"/><path d="M3 17 L13 25 L23 17" fill="none" stroke="var(--card)" stroke-width="1.8"/></svg>
        </span>
        <span>morvex412@morvex.au</span>
      </li>
      <li class="contact-item">
        <span class="contact-icon">
          <svg viewBox="0 0 26 46" aria-hidden="true"><path d="M2 20 Q13 12 24 20 L22 24 L18 22 L18 20 Q13 18 8 20 L8 22 L4 24 Z" fill="var(--icon)"/><path d="M8 23 L18 23 L22 32 L4 32 Z" fill="var(--icon)"/><circle cx="13" cy="27" r="2.5" fill="var(--card)"/></svg>
        </span>
        <span>03 5550 1842</span>
      </li>
    </ul>

    <div class="divider"></div>

    <div class="holder">
      <p class="holder-name">K.Delamere</p>
      <p class="holder-title">My Title</p>
    </div>

    <div class="rule rule--footer-top"></div>
    <div class="ornament-band ornament-band--footer" role="img" aria-label="Grey geometric star-and-knot ornamental border"></div>
    <div class="rule rule--footer-bottom"></div>
  </div>
</div>
</body>
</html>
```